Design Box Packaging with Logo for a high-end menswear store

I would like to come up with a design for our shipping boxes.
- Printing would only be in 1 colour. (box will be in mid beige/brown)
- I want it to look modern and clean
- I have attached my logo
- It is for a high-end menswear store for shipping clothing for online purchases
Size of the box is about 14 x 10 x 5

Target Market(s)

High-end / wealthy people shopping online

Industry/Entity Type

Clothing, retail, online high-end clothing

Colors

Designer to choose colors to be used in the design.

Requirements
Must have
• Look sharp and clean, have logo information, online printing one colour
Nice to have
• Look clean and modern

```html
<!DOCTYPE html>
<html lang="en">
<head>
<meta charset="utf-8">
<title>Maison Lucien – Shipping Box Lid</title>
<link rel="stylesheet" href="https://fonts.googleapis.com/css2?family=Montserrat:wght@400&display=swap">
<style>
  :root {
    --kraft: #c59e6c;
    --kraft-light: #cfa978;
    --kraft-dark: #b98f5d;
    --ink: #0c0a09;
  }
  html, body {
    margin: 0;
    padding: 0;
    width: 700px;
    height: 1200px;
    overflow: hidden;
    background: var(--kraft);
  }
  .box-lid {
    position: relative;
    width: 700px;
    height: 1200px;
    background:
      radial-gradient(ellipse at 30% 20%, var(--kraft-light) 0%, transparent 60%),
      radial-gradient(ellipse at 80% 85%, var(--kraft-dark) 0%, transparent 55%),
      var(--kraft);
  }
  .brand-band {
    position: absolute;
    top: 0;
    left: 128px;
    width: 134px;
    height: 1200px;
    background: var(--ink);
    display: flex;
    align-items: center;
    justify-content: center;
  }
  .brand-mark {
    display: flex;
    flex-direction: column;
    align-items: center;
    gap: 18px;
  }
  .brand-square {
    width: 22px;
    height: 22px;
    background: var(--kraft);
  }
  .brand-name {
    margin: 0;
    font-family: "Montserrat", sans-serif;
    font-weight: 400;
    font-size: 17px;
    line-height: 1.5;
    letter-spacing: 0.28em;
    text-align: center;
    color: var(--kraft);
    padding-left: 0.28em;
  }
</style>
</head>
<body>
  <main class="box-lid">
    <div class="brand-band">
      <div class="brand-mark">
        <span class="brand-square"></span>
        <p class="brand-name">MAISON<br>LUCIEN</p>
      </div>
    </div>
  </main>
</body>
</html>
```